Crestline Lending Group Business Cards

We are looking to revamp the current business cards each of our locations uses. We are a lending company that specializes in personal loans, title loans, and tax services. We have locations in New Mexico, Texas, and Oklahoma.

We would like a cleaner, sleeker look while still highlighting what we offer. Title Loans, Personal Loans & Tax Services. We also want to include our referral fee somewhere on the card. We would like to see an English option as well as a Spanish option for the cards.

PLEASE NOTE: Some business cards do not include the employee's name but just the store's location, while others will include both.

These are double-sided business cards, and we would like to see proof if possible. I have included proofs of our current business cards for you to review below, as well as our company logo. Feel free to get creative with the logo, etc! Colors should match the logo; however, you do not need to use all of our logo colors if you don't want to.

```html
<!DOCTYPE html>
<html lang="en">
<head>
<meta charset="utf-8">
<title>Crestline Lending Group – Business Card Proof</title>
<link rel="stylesheet" href="https://fonts.googleapis.com/css2?family=Figtree:wght@400;500;600;700;800&display=swap">
<style>
  :root {
    --green: #10512f;
    --red: #c1232a;
    --white: #ffffff;
    --ink: #1d1d1d;
    --backdrop: #f7f8fa;
    --font: "Figtree", Arial, sans-serif;
  }
  * { margin: 0; padding: 0; box-sizing: border-box; }
  html, body {
    width: 1200px; height: 1000px; overflow: hidden;
    background: var(--backdrop);
    font-family: var(--font);
  }
  .proof { position: relative; width: 1200px; height: 1000px; }

  .card {
    position: absolute; left: 300px; width: 600px; height: 355px;
    border-radius: 24px; overflow: hidden;
    box-shadow: 0 4px 10px rgba(0,0,0,0.25);
  }

  /* ---------- front ---------- */
  .card-front { top: 118px; background: var(--white); }
  .brand-name {
    position: absolute; left: 22px; top: 40px;
    color: var(--green); font-weight: 700; font-size: 26px; letter-spacing: -0.2px;
  }
  .accent-bar { position: absolute; left: 0; top: 160px; width: 12px; height: 38px; background: var(--red); }
  .person-name {
    position: absolute; left: 21px; top: 154px;
    color: var(--green); font-weight: 800; font-size: 21px; letter-spacing: 0.2px;
  }
  .person-title {
    position: absolute; left: 21px; top: 181px;
    color: var(--ink); font-weight: 500; font-size: 15px;
    padding-bottom: 5px; border-bottom: 2px solid var(--red); width: 148px;
  }
  .contact { position: absolute; left: 20px; top: 227px; list-style: none; color: var(--ink); font-size: 15px; }
  .contact li { display: flex; align-items: flex-start; gap: 6px; line-height: 21px; margin-bottom: 2px; }
  .contact li.address { margin-top: 6px; }
  .contact svg { flex: none; width: 14px; height: 14px; margin-top: 4px; fill: var(--red); }
  .feature-name {
    position: absolute; left: 270px; top: 92px; width: 310px;
    text-align: center; color: var(--green);
    font-weight: 700; font-size: 46px; line-height: 52px;
  }
  .front-web {
    position: absolute; left: 270px; top: 294px; width: 310px; text-align: center;
    color: var(--ink); font-weight: 700; font-size: 15px;
  }
  .services-band {
    position: absolute; left: 0; top: 319px; width: 600px; height: 24px;
    background: var(--red); color: var(--white);
    text-align: center; font-weight: 500; font-size: 16.5px; line-height: 24px;
  }

  /* ---------- back ---------- */
  .card-back { top: 527px; background: var(--red); }
  .back-split { position: absolute; inset: 0; }
  .back-name {
    position: absolute; left: 24px; top: 40px;
    color: var(--white); font-weight: 700; font-size: 38px; line-height: 42px;
  }
  .back-web {
    position: absolute; left: 104px; top: 152px;
    color: var(--red); font-weight: 600; font-size: 15px;
  }
  .refer {
    position: absolute; left: 20px; top: 240px;
    color: var(--white); font-weight: 700; font-size: 46px;
  }
  .offer-get {
    position: absolute; left: 390px; top: 184px;
    color: var(--green); font-weight: 800; font-size: 52px; line-height: 56px;
  }
  .offer-upto {
    position: absolute; left: 500px; top: 188px;
    color: var(--green); font-weight: 600; font-size: 21px; line-height: 20px; text-align: center;
  }
  .offer-amount {
    position: absolute; left: 384px; top: 244px;
    color: var(--white); font-weight: 800; font-size: 86px; line-height: 96px; letter-spacing: -1px;
  }
</style>
</head>
<body>
<main class="proof">

  <section class="card card-front" aria-label="Business card front">
    <p class="brand-name">Crestline Lending Group</p>

    <span class="accent-bar"></span>
    <h1 class="person-name">JANE DOE</h1>
    <p class="person-title">BRANCH MANAGER</p>

    <ul class="contact">
      <li>
        <svg viewBox="0 0 24 24" aria-hidden="true"><path d="M6.6 10.8a15.1 15.1 0 0 0 6.6 6.6l2.2-2.2a1 1 0 0 1 1-.25 11.4 11.4 0 0 0 3.6.57 1 1 0 0 1 1 1V20a1 1 0 0 1-1 1A17 17 0 0 1 3 4a1 1 0 0 1 1-1h3.5a1 1 0 0 1 1 1c0 1.25.2 2.45.57 3.57a1 1 0 0 1-.25 1z"/></svg>
        (505) 555-1212
      </li>
      <li>
        <svg viewBox="0 0 24 24" aria-hidden="true"><path d="M3 5h18a1 1 0 0 1 1 1v.4l-10 6.2L2 6.4V6a1 1 0 0 1 1-1zm-1 3.7 10 6.2 10-6.2V18a1 1 0 0 1-1 1H3a1 1 0 0 1-1-1z"/></svg>
        abcde@crestlinelending.com
      </li>
      <li class="address">
        <svg viewBox="0 0 24 24" aria-hidden="true"><path d="M12 2a7 7 0 0 0-7 7c0 5.2 7 13 7 13s7-7.8 7-13a7 7 0 0 0-7-7zm0 9.5A2.5 2.5 0 1 1 12 6.5a2.5 2.5 0 0 1 0 5z"/></svg>
        <span>123 Elm Street, Suite B<br>Anytown, Texas 55555</span>
      </li>
    </ul>

    <p class="feature-name">Crestline<br>Lending<br>Group</p>
    <p class="front-web">www.CrestlineLending.com</p>

    <p class="services-band">Specializes in Personal loans, Title loans, and Tax services</p>
  </section>

  <section class="card card-back" aria-label="Business card back">
    <svg class="back-split" viewBox="0 0 600 355" aria-hidden="true">
      <polygon points="0,0 600,0 600,2 318,180 0,180" fill="var(--green)"/>
    </svg>

    <p class="back-name">Crestline<br>Lending Group</p>
    <p class="back-web">www.CrestlineLending.com</p>

    <p class="refer">Refer a Friend</p>
    <p class="offer-get">GET</p>
    <p class="offer-upto">up<br>to</p>
    <p class="offer-amount">$100</p>
  </section>

</main>
</body>
</html>
```